Renata Quisby

Luxury And Style -

Black - White & Gold

Target Market(s)

Fashion

Industry/Entity Type

Fashion

Requirements
Must have
• High-End
Nice to have
• We will Print on Silk Paper

```html
<!DOCTYPE html>
<html lang="en">
<head>
<meta charset="utf-8">
<title>Renata Quisby Letterhead</title>
<link href="https://fonts.googleapis.com/css2?family=Poppins:wght@400;500;600&display=swap" rel="stylesheet">
<style>
  :root {
    --backdrop: #f3f3f4;
    --paper: #fbfaf7;
    --gold: #b8934a;
    --ink: #141414;
    --ink-soft: #2a2a2a;
  }
  * { margin: 0; padding: 0; box-sizing: border-box; }
  html, body { width: 900px; height: 1200px; overflow: hidden; background: var(--backdrop); }
  body { font-family: "Poppins", sans-serif; color: var(--ink); }

  .letterhead {
    position: absolute; left: 40px; top: 20px;
    width: 820px; height: 1160px;
    background: var(--paper);
    overflow: hidden;
  }
  .brand-name {
    position: absolute; left: 74px; top: 163px;
    font-size: 14px; font-weight: 400; letter-spacing: 4.6px;
    color: var(--gold); text-transform: uppercase;
  }
  .header-rule {
    position: absolute; left: 74px; top: 197px; width: 671px; height: 1px;
    background: var(--ink);
  }
  .header-rule::before {
    content: ""; position: absolute; left: 0; top: -2px; width: 239px; height: 5px;
    background: var(--gold);
  }

  .recipient-column { position: absolute; left: 74px; top: 296px; width: 240px; font-size: 12.5px; line-height: 18px; }
  .recipient-column h3 { font-size: 15px; font-weight: 600; margin-bottom: 13px; }
  .recipient-column .sender-name { font-weight: 500; margin-top: 45px; margin-bottom: 8px; }
  .recipient-column .letter-date { margin-top: 40px; }
  .recipient-column .letter-date strong { font-weight: 600; }

  .letter-body { position: absolute; left: 339px; top: 300px; width: 406px; }
  .letter-body h2 { font-size: 21px; font-weight: 600; color: var(--gold); line-height: 26px; margin-bottom: 16px; }
  .letter-body p {
    font-size: 10.9px; line-height: 17.9px; text-align: justify; color: var(--ink-soft);
    letter-spacing: -0.1px; margin-bottom: 31px;
  }
  .letter-body p.closing { color: #000; }

  .sign-off { position: absolute; left: 340px; top: 776px; }
  .sign-off .signer-name { font-size: 21px; font-weight: 600; line-height: 26px; }
  .sign-off .signer-role { font-size: 12.5px; line-height: 16px; margin-left: 1px; }
  .signature-area {
    position: absolute; left: 344px; top: 828px; width: 178px; height: 80px;
    background: linear-gradient(120deg, rgba(20,20,20,0.09), rgba(20,20,20,0.03));
    border-radius: 4px;
  }

  .contact-block { position: absolute; top: 1018px; font-size: 11px; line-height: 15px; }
  .contact-block dt { font-size: 12.5px; font-weight: 600; line-height: 17px; }
  .contact-block dd { margin-bottom: 7px; }
  .contact-block.primary { left: 74px; }
  .contact-block.secondary { left: 172px; }
  .contact-divider { position: absolute; left: 155px; top: 1021px; width: 1.5px; height: 65px; background: var(--gold); }

  .footer-mark { position: absolute; right: 74px; top: 1032px; display: flex; align-items: center; gap: 8px; }
  .footer-mark .mark-name { font-size: 11px; letter-spacing: 2px; color: var(--gold); text-transform: uppercase; }
  .footer-mark .mark-circle { width: 52px; height: 52px; border: 1px solid var(--gold); border-radius: 50%; }

  .footer-band { position: absolute; left: 0; bottom: 0; width: 820px; height: 51px; }
</style>
</head>
<body>
  <main class="letterhead">
    <div class="brand-name">Renata Quisby</div>
    <div class="header-rule"></div>

    <section class="recipient-column">
      <h3>To</h3>
      <p>123 Anywhere Address.,<br>Any City, Location Here</p>
      <p class="sender-name">Your Name</p>
      <p>123 Anywhere Address.,<br>Any City, 2nd Location Here</p>
      <p class="letter-date"><strong>Date:</strong> Octobor 06th, 2025</p>
    </section>

    <section class="letter-body">
      <h2>Dear Client</h2>
      <p>Lorem ipsum dolor sit amet, consectetuer adipiscing elit, sed diam nonummy nibh euismod tincidunt ut laoreet dolore magna aliquam erat volutpat. Ut wisi enim ad minim veniam, quis nostrud exerci tation ullamcorper suscipit lobortis nisl ut aliquip ex ea commodo consequat. Duis autem vel eum iriure dolor in hendrerit in vulputate velit esse molestie consequat, vel illum dolore eu feugiat nulla facilisis at vero eros et accumsan et iusto odio dignissim qui blandit praesent luptatum zzril delenit augue duis dolore te feugait nulla facilisi.</p>
      <p>Lorem ipsum dolor sit amet, consectetuer adipiscing elit, sed diam nonummy nibh euismod tincidunt ut laoreet dolore magna aliquam erat volutpat. Ut wisi enim ad minim veniam, quis nostrud exerci tation ullamcorper suscipit lobortis nisl ut aliquip ex ea commodo consequat. Duis autem vel eum iriure dolor in hendrerit in vulputate velit esse molestie consequat,</p>
      <p class="closing">Lorem ipsum dolor sit amet, consectetuer adipiscing elit, sed diam nonummy nibh euismod tincidunt ut laoreet dolore magna aliquam erat volutpat.</p>
    </section>

    <section class="sign-off">
      <div class="signer-name">Elias Marrow</div>
      <div class="signer-role">Manager</div>
    </section>
    <div class="signature-area" role="img" aria-label="Handwritten signature"></div>

    <dl class="contact-block primary">
      <dt>Phone</dt><dd>+1234 56789</dd>
      <dt>Email</dt><dd>+1234 56789</dd>
    </dl>
    <div class="contact-divider"></div>
    <dl class="contact-block secondary">
      <dt>Website</dt><dd>www.yourwebsite.com</dd>
      <dt>Address</dt><dd>www.your address here</dd>
    </dl>

    <div class="footer-mark">
      <span class="mark-name">Renata Quisby</span>
      <span class="mark-circle"></span>
    </div>

    <svg class="footer-band" viewBox="0 1109 820 51" preserveAspectRatio="none" aria-hidden="true">
      <path fill="var(--ink)" d="M0 1134 H400 Q410 1134 415 1128 L431 1109 H820 V1147.5 H410 Q404 1147.5 400 1152 L393 1160 H0 Z"/>
      <path fill="var(--gold)" d="M431 1109 H820 V1113 H428 Z"/>
    </svg>
  </main>
</body>
</html>
```